Veltrop Partners Website - developing a website for a new IIoT (Industrial Internet of Things) startup

Hi All-

Thought I'd re-write this bit...

Firstly, to everyone who has submitted designs, thank you.

Basically, we are looking for a simple/ elegant / modern website with clean lines and design. Because this is a startup, we don't have a great deal of content. Therefore, I'm relying on the site to give us an established / international feel (no images of London, London attractions, or the London skyline please!) We will have offices in London / LA and Tokyo by the end of this year.

Selecting great images is really important. As I say, abstract is fine (less literal.) Black and white is fine as well. We need to convey our expertise to new, international clients, so this is v.important.

http://www.brevanti41.it/ (favourite)
http://www.crafthollowstudio.com/cases/

In terms of colour, I think white /grey/ black and maybe experiment with red for the word Veltrop and (possibly) Group. Please note** I need the following words / strap line written underneath the main logo: IIoT Strategy. Sensor Innovation. Machine Learning.

Whomever we chose to work with, this will be an ongoing partnership: we will continually need to add new content and update the site.

Thank you!

Dell.
Updates

**Please view updated brief description.

Target Market(s)

Mid-sized (£25M- £500M GBP) companies in the UK/ US and Asia. Facilities/ Construction/ Automotive/ Manufacturing / Engineering

Industry/Entity Type

Information Technology

Logo Text

Veltrop Partners -- IIoT Strategy. Sensor Innovation. Machine Learning (written underneath)

Coding

Coded - Design and coding required

Number of Pages Required

5+ page

Font styles to use
Sans Serif

Requirements
Must have
• An international, established, aspirational feel. Beautiful imagery. elegant infographics (nothing complex). CTA on homepage.
Should not have
• Anything cartoony / informal or naff corporate imagery.

```html
<!DOCTYPE html>
<html lang="en">
<head>
<meta charset="utf-8">
<title>Veltrop Partners</title>
<link href="https://fonts.googleapis.com/css2?family=Poppins:wght@300;400;500;600&family=Roboto:wght@300;400;500&display=swap" rel="stylesheet">
<style>
:root{
  --navy:#2a2852;
  --navy-deep:#242246;
  --violet:#8586f4;
  --violet-soft:#a9a9ff;
  --ink:#222233;
  --body:#55566a;
  --muted:#8a8b9c;
  --grey:#f4f4f7;
  --line:#dcdce6;
  --white:#ffffff;
}
*{box-sizing:border-box;margin:0;padding:0}
html,body{width:1200px;height:3020px;overflow:hidden}
body{position:relative;background:var(--white);font-family:"Roboto",sans-serif;color:var(--body)}
.abs{position:absolute}
h2{font-family:"Poppins",sans-serif;font-weight:400;color:var(--ink);font-size:28px;letter-spacing:.3px}
.rule::after{content:"";display:inline-block;width:36px;height:1px;background:var(--line);margin-left:14px;vertical-align:middle}
p{font-size:12.5px;line-height:22px}

/* hero */
.hero{left:0;top:0;width:1200px;height:556px;background:linear-gradient(135deg,#34325f 0%,#2b2955 45%,#363466 70%,#262449 100%)}
.hero-photo{left:0;top:0;width:1200px;height:556px;background:radial-gradient(ellipse at 45% 35%,rgba(120,118,170,.35),transparent 55%),radial-gradient(ellipse at 75% 30%,rgba(110,108,160,.25),transparent 45%)}
.brand{left:88px;top:42px;display:flex;align-items:center;gap:10px;font-family:"Poppins",sans-serif;font-size:17px;color:var(--white);font-weight:400}
.brand-mark{width:9px;height:9px;background:var(--white)}
.menu-btn{left:1066px;top:32px;width:44px;height:44px;border-radius:50%;background:rgba(255,255,255,.12)}
.hero-title{left:0;top:232px;width:1200px;text-align:center;font-family:"Poppins",sans-serif;font-weight:400;font-size:62px;color:var(--white);letter-spacing:.5px}

/* about */
.info-card{left:630px;top:478px;width:480px;height:214px;background:var(--white);padding:58px 46px 0 46px;box-shadow:0 6px 24px rgba(30,30,60,.06)}
.info-card h4{font-family:"Poppins",sans-serif;font-size:10px;letter-spacing:2px;font-weight:500;color:var(--ink);margin-bottom:16px}
.info-card p{font-size:11px;line-height:19px;color:var(--body)}
.index-tile{left:452px;top:558px;width:178px;height:178px;background:var(--violet);display:flex;flex-direction:column;align-items:center;justify-content:center;color:var(--white);font-family:"Poppins",sans-serif;font-size:11px;letter-spacing:2px}
.index-tile span{display:block;width:1px;height:12px;background:rgba(255,255,255,.8);margin:6px 0}
.about-photo{left:632px;top:692px;width:568px;height:354px;background:linear-gradient(120deg,#cbbfae 0%,#e8dcd0 30%,#b7a596 55%,#7e6f68 80%,#5a4c4a 100%)}
.about{left:88px;top:714px;width:390px}
.about h2{margin-bottom:20px}
.about p{margin-bottom:12px}
.btn-outline{display:inline-block;margin-top:22px;width:118px;height:44px;border:1px solid #9a9aa8;font-size:12px;line-height:42px;text-align:center;color:var(--ink)}

/* strategy */
.strategy{left:0;top:1046px;width:1200px;height:360px;background:var(--grey)}
.strat-left{left:88px;top:1120px;width:560px}
.strat-left h2{margin-bottom:20px}
.strat-left p{margin-bottom:12px}
.strat-right{left:676px;top:1120px;width:440px}
.strat-right h2{font-size:26px;line-height:31px;margin-bottom:22px}
.checks{list-style:none}
.checks li{display:flex;align-items:center;gap:12px;font-size:12.5px;margin-bottom:16px;color:var(--body)}
.checks svg{flex:none}

/* sensors */
.sensors-head{left:0;top:1456px;width:1200px;text-align:center}
.sensors-head h2{margin-bottom:18px}
.sensors-head p{font-size:12px;width:780px;margin:0 auto 8px}
.sensor-map{left:0;top:1600px}
.sensor-map text{font-family:"Roboto",sans-serif;font-size:13px;fill:#444556}

/* data & ai */
.data{left:0;top:2060px;width:1200px;height:390px;background:var(--grey)}
.data-head{left:0;top:2104px;width:1200px;text-align:center}
.data-head h2{margin-bottom:20px}
.data-head p{font-size:12px;width:820px;margin:0 auto}
.flow{left:0;top:2270px}
.flow text{font-family:"Roboto",sans-serif;font-size:13px;fill:#444556}

/* events */
.events{left:0;top:2450px;width:1200px;height:288px;background:var(--violet);text-align:center;padding-top:56px}
.events h2{color:var(--white)}
.events h2::after{background:rgba(255,255,255,.5)}
.events p{color:var(--white);font-size:12px;width:760px;margin:14px auto 0}
.signup{left:354px;top:2610px;width:492px;height:46px;display:flex}
.signup-field{flex:1;background:var(--white);display:flex;align-items:center;gap:12px;padding-left:14px;font-size:12px;color:var(--muted)}
.signup-btn{width:50px;background:var(--navy);display:flex;align-items:center;justify-content:center}

/* footer */
.footer{left:0;top:2738px;width:1200px;height:282px;background:var(--navy)}
.contact{top:2800px;width:340px;text-align:center;color:var(--white)}
.contact h5{font-family:"Poppins",sans-serif;font-size:10px;letter-spacing:1.5px;font-weight:600;margin:18px 0 8px}
.contact div{font-size:15px;font-weight:300}
.divider{top:2832px;width:1px;height:64px;background:rgba(255,255,255,.15)}
.footer-rule{left:88px;top:2962px;width:1024px;height:1px;background:rgba(255,255,255,.12)}
.legal{top:2984px;font-size:11.5px;color:var(--white)}
</style>
</head>
<body>

<section class="abs hero">
  <div class="abs hero-photo" role="img" aria-label="Team working together around a laptop, tinted deep navy"></div>
  <div class="abs brand"><span class="brand-mark"></span>Veltrop Partners</div>
  <div class="abs menu-btn">
    <svg width="44" height="44" viewBox="0 0 44 44"><g stroke="#fff" stroke-width="1.6"><line x1="16" y1="17" x2="28" y2="17"/><line x1="16" y1="22" x2="28" y2="22"/><line x1="16" y1="27" x2="28" y2="27"/></g></svg>
  </div>
  <h1 class="abs hero-title">Veltrop Partners</h1>
</section>

<div class="abs info-card">
  <h4>BASIC INFO</h4>
  <p>The core team at Veltrop Partners are Innovators, Engineers, PhDs and Data Scientists who assist mid-sized companies ($25M- $500M) to capitalise on the enormous potential of the Industrial Internet of Things ("IIoT")</p>
</div>
<div class="abs index-tile"><span></span>01<span></span></div>
<div class="abs about-photo" role="img" aria-label="Group of young colleagues smiling at a laptop screen"></div>
<div class="abs about">
  <h2 class="rule">About</h2>
  <p>Our three business units – Strategy, Sensors and AI – mean that we can provide expert advice to both new entrants and companies already familiar with IIoT.</p>
  <p>Founded by our Chief Strategy Officer and serial entrepreneur, Dell Marrow, Veltrop is based in London and have plans to open offices in Tokyo and LA in late 2017.</p>
  <a class="btn-outline">Learn More</a>
</div>

<section class="abs strategy"></section>
<div class="abs strat-left">
  <h2 class="rule">Strategy</h2>
  <p>The Strategy team work with customers to navigate the complex world of IIoT and develop world-class strategies for maximising value. We know that connecting assets is not appropriate for every business: sometimes the challenges outweigh the rewards.</p>
  <p>However, where an IIoT strategy is appropriate we have the right team to help your company clarify its visions, goals &amp; guiding principles and manage the IIoT roadmap in partnership with your senior team</p>
</div>
<div class="abs strat-right">
  <h2 class="rule">Ideas for IIoT strategy<br>development include</h2>
  <ul class="checks">
    <li><svg width="16" height="16" viewBox="0 0 16 16"><circle cx="8" cy="8" r="7" fill="none" stroke="#9a9aa8"/><path d="M5 8.2l2 2 4-4" fill="none" stroke="#9a9aa8" stroke-width="1.2"/></svg>Opportunities for quality and maintenance improvements</li>
    <li><svg width="16" height="16" viewBox="0 0 16 16"><circle cx="8" cy="8" r="7" fill="none" stroke="#9a9aa8"/><path d="M5 8.2l2 2 4-4" fill="none" stroke="#9a9aa8" stroke-width="1.2"/></svg>Potential for offering new services to customers</li>
    <li><svg width="16" height="16" viewBox="0 0 16 16"><circle cx="8" cy="8" r="7" fill="none" stroke="#9a9aa8"/><path d="M5 8.2l2 2 4-4" fill="none" stroke="#9a9aa8" stroke-width="1.2"/></svg>Investigating new data, service or product-centric business models</li>
    <li><svg width="16" height="16" viewBox="0 0 16 16"><circle cx="8" cy="8" r="7" fill="none" stroke="#9a9aa8"/><path d="M5 8.2l2 2 4-4" fill="none" stroke="#9a9aa8" stroke-width="1.2"/></svg>Developing new revenue streams</li>
  </ul>
</div>

<div class="abs sensors-head">
  <h2 class="rule">Sensors</h2>
  <p>The Sensor team are focused on innovation using Sensors and MEMS (Micro-Electromechanical Systems.) We view ourselves as the conduit between the vast array of complex sensors and their potential applications in the 'real world.'</p>
  <p>Our main focus is looking at sensor deployments for Buildings, Environment, Factories, Parking, Agriculture, Water, Air and Health.</p>
</div>

<svg class="abs sensor-map" width="1200" height="420" viewBox="0 0 1200 420">
  <circle cx="598" cy="238" r="161" fill="none" stroke="#e6e6ee" stroke-width="4"/>
  <circle cx="598" cy="238" r="106" fill="#8586f4"/>
  <text x="598" y="244" text-anchor="middle" style="fill:#fff;font-size:18px;font-family:Poppins,sans-serif;letter-spacing:.5px">SENSORS</text>
  <g fill="#fff" stroke="#ececf3" stroke-width="1">
    <circle cx="594" cy="67" r="27"/><circle cx="513" cy="97" r="27"/><circle cx="678" cy="91" r="27"/>
    <circle cx="447" cy="155" r="27"/><circle cx="739" cy="157" r="27"/><circle cx="425" cy="238" r="27"/>
    <circle cx="755" cy="238" r="27"/><circle cx="447" cy="322" r="27"/><circle cx="733" cy="328" r="27"/>
    <circle cx="517" cy="383" r="27"/><circle cx="658" cy="383" r="27"/>
  </g>
  <g fill="none" stroke="#8586f4" stroke-width="1.5" stroke-linecap="round">
    <path d="M590 57v8l-7 12h22l-7-12v-8M588 57h12"/>
    <rect x="502" y="91" width="22" height="10" rx="2"/><path d="M506 101v4M520 101v4"/>
    <circle cx="678" cy="91" r="9"/><path d="M678 91l5-4"/>
    <circle cx="447" cy="155" r="10"/><circle cx="447" cy="155" r="5"/>
    <path d="M732 166l12-12M738 150l3-3M746 158l3-3M744 150l3-3"/>
    <rect x="421" y="226" width="8" height="14" rx="4"/><path d="M417 236a8 8 0 0 0 16 0M425 244v4"/>
    <path d="M746 229v18M755 229v18M764 229v18"/><path d="M743 236h6M752 242h6M761 234h6"/>
    <path d="M436 317q5-4 11 0t11 0M436 323q5-4 11 0t11 0M436 329q5-4 11 0t11 0"/>
    <path d="M730 318v14a5 5 0 1 0 6 0v-14a3 3 0 0 0 -6 0"/><path d="M740 320h4M740 325h4"/>
    <path d="M510 375v12a6 6 0 0 0 12 0M522 381h6"/><circle cx="526" cy="376" r="3"/>
    <path d="M658 372q-8 10-8 15a8 8 0 0 0 16 0q0-5-8-15z"/>
  </g>
  <g>
    <text x="594" y="27" text-anchor="middle">Chemical and gas</text>
    <text x="475" y="101" text-anchor="end">Machine Vision</text>
    <text x="721" y="95">Motion/ Velocity</text>
    <text x="413" y="145" text-anchor="end">Proximity /</text>
    <text x="413" y="164" text-anchor="end">Presence/ Position</text>
    <text x="781" y="161">Acceleration / Tilt</text>
    <text x="393" y="242" text-anchor="end">Sound / Vibration</text>
    <text x="791" y="242">Levels and Leaks</text>
    <text x="411" y="309" text-anchor="end">Water /</text>
    <text x="411" y="328" text-anchor="end">Liquid Flow</text>
    <text x="771" y="334">Temperature</text>
    <text x="469" y="380" text-anchor="end">Pressure/</text>
    <text x="469" y="399" text-anchor="end">Force / Load</text>
    <text x="707" y="378">Moisture and</text>
    <text x="707" y="397">Humidity</text>
  </g>
</svg>

<section class="abs data"></section>
<div class="abs data-head">
  <h2 class="rule">Data &amp; AI</h2>
  <p>The Data &amp; AI team focus on getting the maximum value from our customer's sensors. We are a small team of engineers and data scientists who know that the real value from IIoT comes from the quality of sensor data. We monitor and analyse this data and then deliver it to our customers via stunning dashboards.</p>
</div>
<svg class="abs flow" width="1200" height="120" viewBox="0 0 1200 120">
  <g fill="#fff"><circle cx="191" cy="40" r="36"/><circle cx="395" cy="40" r="36"/><circle cx="600" cy="40" r="36"/><circle cx="805" cy="40" r="36"/><circle cx="1007" cy="40" r="36"/></g>
  <g fill="none" stroke="#b4b4c0" stroke-width="1.2"><path d="M285 40h18M298 36l5 4-5 4M490 40h18M503 36l5 4-5 4M695 40h18M708 36l5 4-5 4M900 40h18M913 36l5 4-5 4"/></g>
  <g fill="none" stroke="#555668" stroke-width="1.4" stroke-linecap="round">
    <ellipse cx="191" cy="30" rx="11" ry="4"/><path d="M180 30v20a11 4 0 0 0 22 0v-20M180 40a11 4 0 0 0 22 0"/>
    <rect x="385" y="26" width="20" height="28" rx="2"/><circle cx="395" cy="36" r="4"/><path d="M389 46h12M389 50h8"/>
    <circle cx="600" cy="40" r="14"/><path d="M600 40l7-7M590 40h3M600 30v3"/>
    <rect x="790" y="28" width="30" height="20"/><path d="M794 42l7-7 5 5 9-9M805 48v6M799 54h12"/>
    <circle cx="1007" cy="40" r="5"/><path d="M991 40h11M1012 40h11M1007 24v11M1007 45v11"/><circle cx="1007" cy="24" r="2"/>
  </g>
  <g fill="#8586f4"><path d="M1020 36l4 4-4 4z"/><path d="M994 36l-4 4 4 4z"/><circle cx="606" cy="52" r="4"/></g>
  <g text-anchor="middle">
    <text x="191" y="106">Rich data</text><text x="395" y="106">Realtime Analytics</text><text x="600" y="106">Historical Analytics</text><text x="805" y="106">Predictive Analytics</text><text x="1007" y="106">Intelligent Decision Making</text>
  </g>
</svg>

<section class="abs events">
  <h2 class="rule">Events</h2>
  <p>However, where an IIoT strategy is appropriate we have the right team to help your company clarify its visions, goals &amp; guiding principles and manage the IIoT roadmap in partnership with your senior team</p>
</section>
<div class="abs signup">
  <div class="signup-field"><svg width="14" height="10" viewBox="0 0 14 10"><rect x=".5" y=".5" width="13" height="9" fill="none" stroke="#9a9aa8"/><path d="M.5 .5l6.5 5 6.5-5" fill="none" stroke="#9a9aa8"/></svg>Email address</div>
  <div class="signup-btn"><svg width="16" height="16" viewBox="0 0 16 16"><path d="M1 7l14-6-5 14-2-6z" fill="#fff"/></svg></div>
</div>

<footer class="abs footer"></footer>
<div class="abs contact" style="left:430px;margin-left:-340px">
  <svg width="30" height="22" viewBox="0 0 30 22"><rect x="1" y="1" width="28" height="20" fill="none" stroke="#fff" stroke-width="1.4"/><path d="M1 1l14 11 14-11M1 21l10-9M29 21l-10-9" fill="none" stroke="#fff" stroke-width="1.4"/></svg>
  <h5>EMAIL ADDRESS:</h5><div>info@veltroppartners.com</div>
</div>
<div class="abs divider" style="left:430px"></div>
<div class="abs contact" style="left:430px">
  <svg width="22" height="26" viewBox="0 0 22 26"><path d="M11 25s-9-9-9-15a9 9 0 0 1 18 0c0 6-9 15-9 15z" fill="none" stroke="#fff" stroke-width="1.4"/><circle cx="11" cy="10" r="3.5" fill="none" stroke="#fff" stroke-width="1.4"/></svg>
  <h5>ADDRESS:</h5><div>Some address line goes here.</div>
</div>
<div class="abs divider" style="left:770px"></div>
<div class="abs contact" style="left:770px">
  <svg width="24" height="24" viewBox="0 0 24 24"><path d="M5 2l4 5-2 3c1.5 3 4 5.5 7 7l3-2 5 4-3 3C10 22 2 14 2 5z" fill="none" stroke="#fff" stroke-width="1.4"/></svg>
  <h5>PHONE NUMBER:</h5><div>123 - 456 - 7890</div>
</div>
<div class="abs footer-rule"></div>
<div class="abs legal" style="left:88px">© 2017, All Rights Reserved.</div>
<div class="abs legal" style="left:888px">Terms &amp; Conditions &nbsp;&nbsp;&nbsp;|&nbsp;&nbsp;&nbsp; Privacy Policy</div>

</body>
</html>
```